Creative Businesss Card desgin!

Create a business card for our business Gleam window cleaning!
We are open to creative ideas as long as it maintains a professional image.

Target Market(s)

Small Commercial window cleaning clients including car dealerships, strata manager, cafe

Industry/Entity Type

Window Cleaning

Contact Information for Business Card

Daniel Prescott
General Manager
Gleam Window Cleaning

daniel@gleamservices.com.au
pane-care-southbank.com.au
Ph: 1800 GET GLEAM
Mob: 0437 582 061

Colors
fbed22
0392cd

Requirements
Should not have
• Stock window cleaning/ squeegee graphics

```html
<!DOCTYPE html>
<html lang="en">
<head>
<meta charset="utf-8">
<title>Gleam Window Cleaning – Business Card</title>
<link rel="stylesheet" href="https://fonts.googleapis.com/css2?family=Arimo:wght@700&family=Noto+Sans:wght@700&family=Mulish:wght@400;700&family=Didact+Gothic&display=swap">
<style>
  :root {
    --navy: #265c87;
    --ink: #2a5a85;
    --yellow: #f5ec35;
    --white: #ffffff;
    --rule: #d6d6d6;
    --bg-top: #efefef;
    --bg-bottom: #a5a5a5;
  }
  * { box-sizing: border-box; margin: 0; padding: 0; }
  html, body { width: 1200px; height: 1200px; overflow: hidden; }
  body {
    position: relative;
    background: linear-gradient(180deg, var(--bg-top) 0%, var(--bg-bottom) 100%);
  }

  .card { position: absolute; left: 166px; width: 868px; height: 510px; }

  /* Front */
  .card-front { top: 74px; background: var(--navy); }
  .brand {
    position: absolute; left: 0; right: 0; top: 228px;
    text-align: center;
    font-family: "Arimo", Arial, sans-serif;
    font-weight: 700;
    color: var(--yellow);
    line-height: 1;
  }
  .brand-name { display: block; font-size: 140px; letter-spacing: 4px; }
  .brand-tagline { display: block; font-size: 47px; margin-top: 12px; }
  .web-row {
    position: absolute; left: 0; right: 0; top: 460px;
    display: flex; align-items: center; gap: 12px;
  }
  .web-row .line { flex: 1; height: 3px; background: var(--yellow); }
  .web-address {
    font-family: "Noto Sans", Verdana, sans-serif;
    font-weight: 700; font-size: 24px; color: var(--white);
    letter-spacing: 0.3px;
  }

  /* Back */
  .card-back { top: 641px; background: var(--white); }
  .person {
    position: absolute; left: 50px; width: 262px; top: 205px;
    text-align: center; color: var(--ink);
    font-family: "Mulish", sans-serif;
  }
  .person-name { font-weight: 700; font-size: 31px; line-height: 1.1; }
  .person-title { font-family: "Didact Gothic", sans-serif; font-size: 23px; line-height: 1.2; margin-top: 2px; }
  .person-mobile { font-weight: 700; font-size: 26px; letter-spacing: 1px; line-height: 1.2; }
  .divider {
    position: absolute; left: 331px; top: 178px; width: 2px; height: 150px;
    background: linear-gradient(180deg, transparent, var(--rule) 20%, var(--rule) 80%, transparent);
  }
  .contact-list { position: absolute; left: 360px; top: 178px; list-style: none; }
  .contact-item {
    display: flex; align-items: flex-start; gap: 13px;
    font-family: "Didact Gothic", sans-serif; font-size: 27px;
    color: var(--ink); line-height: 33px; margin-bottom: 11px;
  }
  .contact-item svg { flex: none; width: 31px; height: 31px; margin-top: 1px; }
  .contact-item span { padding-left: 18px; }
</style>
</head>
<body>

<section class="card card-front">
  <h1 class="brand">
    <span class="brand-name">GLEAM</span>
    <span class="brand-tagline">WINDOW CLEANING</span>
  </h1>
  <div class="web-row">
    <span class="line"></span>
    <span class="web-address">pane-care-southbank.com.au</span>
    <span class="line"></span>
  </div>
</section>

<section class="card card-back">
  <div class="person">
    <p class="person-name">Daniel Prescott</p>
    <p class="person-title">General Manager</p>
    <p class="person-mobile">0437 582 061</p>
  </div>
  <div class="divider"></div>
  <ul class="contact-list">
    <li class="contact-item">
      <svg viewBox="0 0 32 32" aria-hidden="true"><circle cx="16" cy="16" r="14.5" fill="none" stroke="#2a5a85" stroke-width="1.5"/><path d="M16 24c-3-4-5-6.5-5-9a5 5 0 0 1 10 0c0 2.5-2 5-5 9z" fill="none" stroke="#2a5a85" stroke-width="1.6"/><circle cx="16" cy="15" r="1.6" fill="#2a5a85"/></svg>
      <span>1207/45 Harbour Row,<br>Southbank VIC 3006</span>
    </li>
    <li class="contact-item">
      <svg viewBox="0 0 32 32" aria-hidden="true"><circle cx="16" cy="16" r="14.5" fill="none" stroke="#2a5a85" stroke-width="1.5"/><rect x="10" y="12" width="12" height="8.5" fill="none" stroke="#2a5a85" stroke-width="1.3"/><path d="M10 12l6 5 6-5M10 20.5l4.5-4M22 20.5l-4.5-4" fill="none" stroke="#2a5a85" stroke-width="1.1"/></svg>
      <span>daniel@gleamservices.com.au</span>
    </li>
    <li class="contact-item">
      <svg viewBox="0 0 32 32" aria-hidden="true"><circle cx="16" cy="16" r="14.5" fill="none" stroke="#2a5a85" stroke-width="1.5"/><path d="M9 14c0-2 3-3 7-3s7 1 7 3v1.5h-3.5v-1.5h-7v1.5H9z" fill="#2a5a85"/><path d="M11.5 16.5h9l1.5 5H10z" fill="#2a5a85"/><circle cx="16" cy="19" r="1.3" fill="#fff"/></svg>
      <span>1800 GET GLEAM</span>
    </li>
  </ul>
</section>

</body>
</html>
```